New Flyer Design Project

Needing brochure explaining the benefits of a home sleep study compared to a clinical hospital sleep study. We had our company logo designed by Vantro Works, we love it. We would like for it to be a bi-fold. See attachments for examples of information we would like to include.

```html
<!DOCTYPE html>
<html lang="en">
<head>
<meta charset="utf-8">
<title>Northfield Sleep Care – Home Sleep Study Bi-fold</title>
<link href="https://fonts.googleapis.com/css2?family=Montserrat:wght@400;500;600;700;800;900&display=swap" rel="stylesheet">
<style>
:root{
  --navy:#0d3c84;
  --navy-dark:#0a2f6b;
  --green:#6bbf3b;
  --ink:#1b2a4a;
  --page:#ffffff;
  --bg:#e4e6ea;
}
*{box-sizing:border-box;margin:0;padding:0}
html,body{width:1200px;height:3202px;overflow:hidden}
body{background:var(--bg);font-family:'Montserrat',sans-serif;color:var(--ink);position:relative}
.spread{position:absolute;left:60px;width:1080px;height:768px;background:var(--page);box-shadow:0 10px 30px rgba(0,0,0,.18);overflow:hidden}
.spread--outside{top:791px}
.spread--inside{top:1643px}
.panel{position:absolute;top:0;width:540px;height:768px;overflow:hidden}
.panel--left{left:0}
.panel--right{left:540px}
.abs{position:absolute}
.brand{display:flex;align-items:center;gap:12px;font-weight:700;color:var(--navy)}
.brand__dot{width:34px;height:34px;border-radius:50%;background:var(--green)}
.rule-green{height:3px;background:var(--green)}
h2,h3{font-weight:800;line-height:1.02;text-transform:uppercase}
.navy{color:var(--navy)}
.green{color:var(--green)}
.body-copy{font-size:12.5px;line-height:1.32;color:var(--navy);font-weight:500}
.checklist{border:2px dashed var(--green);border-radius:10px;display:flex;gap:18px;padding:10px 12px;font-size:11.5px;font-weight:600;color:var(--navy)}
.checklist__col{display:flex;flex-direction:column;gap:7px}
.checklist__col--a{width:208px}
.checklist__col--b{flex:1}
.check{display:flex;gap:7px;align-items:flex-start;line-height:1.2}
.check::before{content:"";flex:0 0 10px;height:10px;border:1px solid #8a94a8;margin-top:2px}
.btn{background:var(--green);color:#fff;font-size:11.5px;font-weight:600;border-radius:5px;padding:9px 12px;white-space:nowrap}
.contact-band{background:var(--navy);color:#fff;font-size:14px;font-weight:500;padding-left:48px;display:flex;flex-direction:column;justify-content:center;gap:11px}
.contact{display:flex;align-items:center;gap:12px}
.contact svg{width:14px;height:14px;flex:0 0 14px}
.delivery{background:var(--navy);border-radius:12px;color:#fff;font-size:16px;font-weight:500;line-height:1.2;display:flex;align-items:center;gap:26px;padding-left:26px}
.feature{position:absolute;left:52px;display:flex;align-items:center;gap:24px}
.feature__icon{flex:0 0 86px;width:86px;height:86px;border-radius:50%;background:var(--navy);border:4px solid var(--green);outline:3px solid #fff;outline-offset:-8px;display:flex;align-items:center;justify-content:center}
.feature__icon svg{width:42px;height:42px}
.feature__title{font-size:26px;font-weight:800;color:var(--green);line-height:1.1;white-space:nowrap}
.feature__text{font-size:16px;font-weight:500;color:var(--navy);line-height:1.1;white-space:nowrap}
.vs{position:absolute;left:484px;top:29px;width:112px;height:112px;border-radius:50%;background:var(--navy);border:5px solid var(--green);color:#fff;font-weight:800;font-size:36px;display:flex;align-items:center;justify-content:center;z-index:2}
</style>
</head>
<body>

<section class="spread spread--outside">
  <div class="panel panel--left">
    <div class="brand abs" style="left:55px;top:66px;font-size:34px"><span class="brand__dot"></span>Northfield Sleep Care</div>
    <div class="rule-green abs" style="left:55px;top:150px;width:430px"></div>
    <h2 class="navy abs" style="left:52px;top:178px;font-size:31px">80% of sleep apnea<br>cases go undiagnosed.</h2>
    <div class="body-copy abs" style="left:52px;top:258px;width:440px">
      <p>Your wake up exhausted. You fall asleep at your desk. Your partner says you stop breathing at night. You know something's wrong.</p>
      <p style="margin-top:12px">Most people wait years before getting tested because sleep labs are expensive, inconvenient, and scheduled months out. Meanwhile you're crashing your car, destroying your health, and feeling like garbage every single day.</p>
    </div>
    <h3 class="abs navy" style="left:50px;top:390px;font-size:21px;font-weight:700">Self assessment checklist<br><span class="green">Do you</span></h3>
    <div class="checklist abs" style="left:52px;top:456px;width:456px">
      <div class="checklist__col checklist__col--a">
        <div class="check">Snore loudly</div>
        <div class="check">Wake up gasping or choking?</div>
        <div class="check">Fall asleep during the day even when you slept 8 hours?</div>
      </div>
      <div class="checklist__col checklist__col--b">
        <div class="check">Wake up with headaches?</div>
        <div class="check">Feel tired no matter how much you sleep?</div>
      </div>
    </div>
    <p class="abs navy" style="left:52px;top:574px;font-size:11.5px;font-weight:700;line-height:1.2;width:270px">If you checked 2 boxes, you probably have sleep apnea. Stop guessing. Get tested.</p>
    <div class="btn abs" style="left:343px;top:571px">Take the sleep quiz now</div>
    <div class="contact-band abs" style="left:0;top:622px;width:540px;height:146px">
      <div class="contact"><svg viewBox="0 0 24 24" fill="none" stroke="#fff" stroke-width="2"><path d="M5 3h4l2 5-3 2a12 12 0 0 0 6 6l2-3 5 2v4a2 2 0 0 1-2 2A18 18 0 0 1 3 5a2 2 0 0 1 2-2z"/></svg>(555) 014-2277</div>
      <div class="contact"><svg viewBox="0 0 24 24" fill="none" stroke="#fff" stroke-width="2"><circle cx="12" cy="12" r="10"/><path d="M2 12h20M12 2c3 3 3 17 0 20M12 2c-3 3-3 17 0 20"/></svg>northfieldsleepcare.com</div>
      <div class="contact"><svg viewBox="0 0 24 24" fill="none" stroke="#fff" stroke-width="2"><path d="M12 22s7-7 7-12a7 7 0 0 0-14 0c0 5 7 12 7 12z"/><circle cx="12" cy="10" r="2.5"/></svg>Local care. Better sleep. Healthier lives.</div>
    </div>
  </div>

  <div class="panel panel--right">
    <h2 class="abs" style="left:40px;top:36px;font-size:43px;line-height:1"><span class="navy">Better sleep</span><br><span class="green">Starts at home</span></h2>
    <p class="abs navy" style="left:40px;top:140px;font-size:22px;font-weight:600">Simple. Comfortable. Effective.</p>
    <svg class="abs" style="left:0;top:176px" width="540" height="460" viewBox="0 0 540 460" preserveAspectRatio="none">
      <defs><linearGradient id="navyFade" x1="0" y1="0" x2="0" y2="1"><stop offset="0" stop-color="#0d3c84"/><stop offset=".55" stop-color="#0d3c84"/><stop offset="1" stop-color="#0d3c84" stop-opacity="0"/></linearGradient></defs>
      <path d="M0 50 Q250 -5 540 25 V460 H0Z" fill="#6bbf3b"/>
      <path d="M0 62 Q250 8 540 38 V460 H0Z" fill="url(#navyFade)"/>
    </svg>
    <p class="abs" style="left:40px;top:248px;font-size:22px;font-weight:500;color:#fff;line-height:1.27">Home Sleep Studies<br>for Better Answers and<br>Better Tomorrows</p>
    <div class="abs" role="img" aria-label="Photo of a woman sleeping peacefully on white pillows" style="left:0;top:345px;width:540px;height:290px;background:linear-gradient(180deg,rgba(13,60,132,0) 0%,#c9ccd3 35%,#eceef1 75%,#ffffff 100%)"></div>
    <div class="brand abs" style="left:120px;top:606px;font-size:28px"><span class="brand__dot" style="width:28px;height:28px"></span>Northfield Sleep Care</div>
    <div class="delivery abs" style="left:41px;top:675px;width:457px;height:68px">
      <svg width="46" height="34" viewBox="0 0 46 34" fill="none" stroke="#6bbf3b" stroke-width="2.4"><path d="M2 6h26v18H2zM28 12h9l7 7v5H28z"/><circle cx="10" cy="27" r="4" fill="#0d3c84"/><circle cx="36" cy="27" r="4" fill="#0d3c84"/></svg>
      <span>We deliver. You sleep.<br>We help you feel like yourself again.</span>
    </div>
  </div>
</section>

<section class="spread spread--inside">
  <div class="vs">VS</div>
  <div class="panel panel--left">
    <h2 class="abs" style="left:52px;top:38px;font-size:30px;line-height:1"><span class="navy">Home sleep study</span><br><span class="green">The smarter choice</span></h2>
    <p class="abs navy" style="left:52px;top:112px;font-size:12.5px;font-weight:500;line-height:1.25;width:420px">A home sleep study is a simple, safe, and effective way to test sleep apnea from the comfort of your own bed.</p>
    <div class="abs" style="left:52px;top:166px;width:440px;height:2px;background:linear-gradient(90deg,var(--navy),rgba(13,60,132,.05))"></div>
    <div class="feature" style="top:190px"><div class="feature__icon"><svg viewBox="0 0 24 24" fill="none" stroke="#fff" stroke-width="1.8"><circle cx="12" cy="12" r="9"/><path d="M8 12l3 3 5-6"/></svg></div><div><div class="feature__title">Comfortable</div><div class="feature__text">A minimal device with 2 wire<br>and 3 sensors</div></div></div>
    <div class="feature" style="top:300px"><div class="feature__icon"><svg viewBox="0 0 24 24" fill="none" stroke="#fff" stroke-width="1.8"><circle cx="12" cy="12" r="9"/><path d="M12 7v5l3 2"/></svg></div><div><div class="feature__title">Convenient</div><div class="feature__text">Delivered to you door-sleep in<br>your own bed at home</div></div></div>
    <div class="feature" style="top:410px"><div class="feature__icon"><svg viewBox="0 0 24 24" fill="none" stroke="#fff" stroke-width="1.8"><path d="M12 3v18M3 12h18"/><circle cx="12" cy="12" r="4"/></svg></div><div><div class="feature__title">Accessible</div><div class="feature__text">Scheduling and device<br>delivery in 2-4 business deys</div></div></div>
    <div class="feature" style="top:522px"><div class="feature__icon"><svg viewBox="0 0 24 24" fill="none" stroke="#fff" stroke-width="1.8"><circle cx="12" cy="12" r="9"/><path d="M15 9c-1-1.5-6-1.5-6 1s6 1.5 6 4-5 2.5-6 1M12 6v12"/></svg></div><div><div class="feature__title">Affordable</div><div class="feature__text">Pay a one-time flat fee of $ 189</div></div></div>
    <div class="contact-band abs" style="left:0;top:624px;width:540px;height:144px">
      <div class="contact"><svg viewBox="0 0 24 24" fill="none" stroke="#fff" stroke-width="2"><path d="M5 3h4l2 5-3 2a12 12 0 0 0 6 6l2-3 5 2v4a2 2 0 0 1-2 2A18 18 0 0 1 3 5a2 2 0 0 1 2-2z"/></svg>(555) 014-2277</div>
      <div class="contact"><svg viewBox="0 0 24 24" fill="none" stroke="#fff" stroke-width="2"><circle cx="12" cy="12" r="10"/><path d="M2 12h20M12 2c3 3 3 17 0 20M12 2c-3 3-3 17 0 20"/></svg>northfieldsleepcare.com</div>
      <div class="contact"><svg viewBox="0 0 24 24" fill="none" stroke="#fff" stroke-width="2"><path d="M12 22s7-7 7-12a7 7 0 0 0-14 0c0 5 7 12 7 12z"/><circle cx="12" cy="10" r="2.5"/></svg>Local care. Better sleep. Healthier lives.</div>
    </div>
  </div>

  <div class="panel panel--right">
    <h2 class="abs" style="left:74px;top:38px;font-size:30px;line-height:1"><span class="navy">Home sleep study</span><br><span class="green">In-lab testing</span></h2>
    <div class="abs" style="left:74px;top:166px;width:440px;height:2px;background:linear-gradient(90deg,var(--navy),rgba(13,60,132,.05))"></div>
    <div class="feature" style="top:190px;left:56px"><div class="feature__icon"><svg viewBox="0 0 24 24" fill="none" stroke="#fff" stroke-width="1.8"><circle cx="12" cy="8" r="4"/><path d="M5 21c0-4 3-7 7-7s7 3 7 7"/></svg></div><div><div class="feature__title">Invasive</div><div class="feature__text">20-30 wires attached all<br>over your body</div></div></div>
    <div class="feature" style="top:300px;left:56px"><div class="feature__icon"><svg viewBox="0 0 24 24" fill="none" stroke="#fff" stroke-width="1.8"><circle cx="12" cy="12" r="8"/><path d="M12 8v4M12 15v1"/></svg></div><div><div class="feature__title">Disruptive</div><div class="feature__text">Must sleep in a lab overnight<br>and requires travel</div></div></div>
    <div class="feature" style="top:410px;left:56px"><div class="feature__icon"><svg viewBox="0 0 24 24" fill="none" stroke="#fff" stroke-width="1.8"><rect x="3" y="5" width="18" height="16" rx="2"/><path d="M3 10h18M8 3v4M16 3v4"/></svg></div><div><div class="feature__title">Hard to schedule</div><div class="feature__text">Scheduling can take anywhere from 3<br>weeks to 6 months</div></div></div>
    <div class="feature" style="top:526px;left:56px"><div class="feature__icon"><svg viewBox="0 0 24 24" fill="none" stroke="#fff" stroke-width="1.8"><path d="M4 20V12M10 20V8M16 20V4"/><path d="M3 21h18"/></svg></div><div><div class="feature__title">Expensive</div><div class="feature__text">Fees can range from $500-$10,000</div></div></div>
    <div class="delivery abs" style="left:41px;top:678px;width:457px;height:68px">
      <svg width="46" height="34" viewBox="0 0 46 34" fill="none" stroke="#6bbf3b" stroke-width="2.4"><path d="M2 6h26v18H2zM28 12h9l7 7v5H28z"/><circle cx="10" cy="27" r="4" fill="#0d3c84"/><circle cx="36" cy="27" r="4" fill="#0d3c84"/></svg>
      <span>We deliver. You sleep.<br>We help you feel like yourself again.</span>
    </div>
  </div>
</section>

</body>
</html>
```